Business card design needed

Front of Card:
I would like to have nearly 3/4 of the card from the top in a Pea Green Colour with the word 'Loftwhirl' written in a(Watermelon Red colour) in the font 'Viner Hand ITC'. Loftwhirl to be written within the Green colour of the card.

The lower 1/3 of the card I would like to have white with the words:
Home and Garden Styling smaller than the word Loftwhirl in Black in the font 'Batang', centred underneath the green section.

At the very bottom in one corner in smaller print I would like to have my contact phone number: Bea M:0419736204 and then the email address:
E: loftwhirlstyling@pemblenet.example on the other side.

Back of Card:
Back of Card to be White
On one side (Left)
I would like the Heading "Garden" in the same pea green colour as the front and in the Viner Hand ITC font. On the other half of the card I would like 'Home' in the Watermelon Red Colour (same as front colour) and in the font Viner Hand ITC.
Underneath these Headings I would like written in black and in Batang font the following list of services.

Garden Home
Garden Styling Interior Styling
Plant Selection Furniture Selection/Arrangement Garden Maintenance Setting Up Home (after move)
Hedging/Mowing Merchandise and Stylist for
Work w/Local Nurseries Marnet and Crabb

Industry/Entity Type

Business

Contact Information for Business Card

Loftwhirl
Home and Garden Styling
M: 0419736204 E: loftwhirlstyling@pemblenet.example

```html
<!DOCTYPE html>
<html lang="en">
<head>
<meta charset="utf-8">
<title>Loftwhirl – Business Card</title>
<link rel="stylesheet" href="https://fonts.googleapis.com/css2?family=Kalam:wght@700&family=Nanum+Myeongjo:wght@400&display=swap">
<style>
  :root {
    --pea-green: #1f7a37;
    --watermelon: #e84d6f;
    --paper: #ffffff;
    --backdrop: #ececec;
    --ink: #222222;
    --ink-soft: #4a4a4a;
    --edge: #d2d2d2;
    --script: "Kalam", cursive;
    --serif: "Nanum Myeongjo", serif;
  }
  html, body {
    margin: 0;
    padding: 0;
    width: 1063px;
    height: 1200px;
    overflow: hidden;
    background: var(--backdrop);
  }
  .canvas {
    position: relative;
    width: 1063px;
    height: 1200px;
  }
  .card {
    position: absolute;
    left: 78px;
    width: 876px;
    height: 486px;
    background: var(--paper);
    border: 1px solid var(--edge);
    box-shadow: 6px 8px 14px rgba(0,0,0,0.12);
    overflow: hidden;
  }
  .card--front { top: 89px; }
  .card--back { top: 608px; }

  .front-panel {
    position: absolute;
    left: 0; top: 0;
    width: 100%;
    height: 282px;
    background: var(--pea-green);
  }
  .divider-band {
    position: absolute;
    left: 0;
    width: 100%;
    height: 30px;
  }
  .card--front .divider-band { top: 288px; }
  .card--back .divider-band { top: 136px; height: 28px; }

  .brand-name {
    position: absolute;
    left: 0; right: 0;
    top: 40px;
    margin: 0;
    text-align: center;
    font-family: var(--script);
    font-weight: 700;
    font-size: 156px;
    line-height: 1;
    color: var(--watermelon);
    letter-spacing: 2px;
  }
  .tagline {
    position: absolute;
    left: 0; right: 0;
    top: 324px;
    margin: 0;
    text-align: center;
    font-family: var(--serif);
    font-weight: 400;
    font-size: 48px;
    color: var(--ink);
  }
  .contact {
    position: absolute;
    top: 418px;
    display: flex;
    align-items: center;
    gap: 8px;
    font-family: var(--serif);
    font-size: 26px;
    color: var(--ink);
  }
  .contact--phone { left: 88px; }
  .contact--email { left: 334px; }
  .contact svg { flex: none; }

  .column-heading {
    position: absolute;
    top: 48px;
    margin: 0;
    font-family: var(--script);
    font-weight: 700;
    font-size: 58px;
    line-height: 1;
  }
  .column-heading--garden { left: 114px; color: var(--pea-green); }
  .column-heading--home { left: 568px; color: var(--watermelon); }

  .service-list {
    position: absolute;
    top: 228px;
    margin: 0;
    padding: 0;
    list-style: none;
    font-family: var(--serif);
    font-size: 23px;
    line-height: 38px;
    color: var(--ink-soft);
  }
  .service-list--garden { left: 66px; }
  .service-list--home { left: 442px; }
  .service-list li {
    position: relative;
    padding-left: 18px;
  }
  .service-list li::before {
    content: "";
    position: absolute;
    left: 0;
    top: 16px;
    width: 8px;
    height: 8px;
    border-radius: 50%;
  }
  .service-list--garden li::before { background: var(--pea-green); }
  .service-list--home li::before { background: var(--watermelon); }
</style>
</head>
<body>
<main class="canvas">

  <section class="card card--front" aria-label="Front of card">
    <div class="front-panel"></div>
    <h1 class="brand-name">Loftwhirl</h1>
    <svg class="divider-band" viewBox="0 0 876 30" preserveAspectRatio="none" aria-hidden="true">
      <rect x="0" y="0" width="876" height="30" fill="var(--pea-green)"/>
      <polygon points="0,0 465,0 434,30 0,30" fill="var(--watermelon)"/>
    </svg>
    <p class="tagline">Home and Garden Styling</p>
    <div class="contact contact--phone">
      <svg width="20" height="24" viewBox="0 0 20 24" aria-hidden="true">
        <path d="M5 1 L9 6 L6.5 9 C7.5 12 9.5 15 12.5 17 L15 14.5 L19 19 L16 22.5 C9 21 3 13 2 4 Z" fill="var(--ink)"/>
      </svg>
      <span>0419736204</span>
    </div>
    <div class="contact contact--email">
      <svg width="26" height="18" viewBox="0 0 26 18" aria-hidden="true">
        <rect x="1" y="1" width="24" height="16" fill="none" stroke="var(--ink)" stroke-width="1.6"/>
        <polyline points="1,1 13,10 25,1" fill="none" stroke="var(--ink)" stroke-width="1.6"/>
      </svg>
      <span>loftwhirlstyling@pemblenet.example</span>
    </div>
  </section>

  <section class="card card--back" aria-label="Back of card">
    <h2 class="column-heading column-heading--garden">Garden</h2>
    <h2 class="column-heading column-heading--home">Home</h2>
    <svg class="divider-band" viewBox="0 0 876 28" preserveAspectRatio="none" aria-hidden="true">
      <rect x="0" y="0" width="876" height="28" fill="var(--watermelon)"/>
      <polygon points="0,0 462,0 419,28 0,28" fill="var(--pea-green)"/>
    </svg>
    <ul class="service-list service-list--garden">
      <li>Garden Styling</li>
      <li>Plant Selection</li>
      <li>Garden Maintenance</li>
      <li>Hedging/Mowing</li>
      <li>Work w/Local Nurseries</li>
    </ul>
    <ul class="service-list service-list--home">
      <li>Interior Styling</li>
      <li>Furniture Selection/Arrangement</li>
      <li>Setting Up Home (after move)</li>
      <li>Merchandise and Stylist<br>for Marnet &amp; Crabb</li>
    </ul>
  </section>

</main>
</body>
</html>
```